Web design for boutique law firm

Web design for law firm; practice areas include:
-international intellectual property counseling
-general corporate (contract negotiation, licensing, distribution agreements
-see my *very* outdated website at www.tbkcounsel.com: here is some of the home page content:

"TBK Law Group enjoys providing proactive, business-minded, efficient legal solutions for individuals and companies that benefit from major law firm experience at reasonable rates.

Some areas of emphasis include:

Counseling individuals and companies with respect to clearing, selecting, securing, managing, commercializing, and protecting intellectual property assets around the world. This includes traditional global brand management, marketing, advertising, and enforcement work as well as litigation.
TBK Law Group also provides general counseling services for individuals and businesses, from start-up advice to sophisticated business transactions strategy, agreement negotiating, dispute resolution, and litigation.
Before founding TBK Law Group in 2008, Curtis P. Langford led the Trademark, Copyright, & Brand Management Group for Halbrook & Pemberly's Seattle office. Curtis was also a senior associate at Silicon Valley based Thackery, Olmsted, Vance, & Bellweather."

Target Market(s)

Clients/potential clients needing tier one, international intellectual property advice with "mega" law firm experience for much less than what we were/would be charging at the "mega firms".

Industry/Entity Type

Legal

Number of Pages Required

4 page

Font styles to use
Serif
Sans Serif

Colors

Designer to choose colors to be used in the design.

Requirements
Must have
• +Improvement over everything on current site at www.tbkcounsel.com.
• +Pictures/bios for me and my team (four of us right now).
• +Easy to update and add/remove content.
• +Must be superior in design (look, feel, ease of use, classy and elegant, but hip, reflects international practice).
• +i have logos and color schemes (see current website) but will consider improvements.
Nice to have
• Let me know your thoughts.
Should not have
• No cheese; no overt sales pitches or marketing (since law firm).

```html
<!DOCTYPE html>
<html lang="en">
<head>
<meta charset="utf-8">
<title>Curtis P. Langford — TBK Law Group</title>
<link rel="stylesheet" href="https://fonts.googleapis.com/css2?family=Open+Sans:wght@400;600;700&display=swap">
<style>
  :root {
    --accent: #f26531;
    --ink: #333333;
    --muted: #444444;
    --paper: #ffffff;
    --footer-bg: #333333;
    --footer-ink: #e6e6e6;
    --portrait-light: #d4d4d4;
    --portrait-dark: #5a5a5a;
  }
  * { box-sizing: border-box; margin: 0; padding: 0; }
  html, body {
    width: 1112px; height: 1200px; overflow: hidden;
    background: var(--paper);
    font-family: "Open Sans", Arial, sans-serif;
    color: var(--ink);
  }
  .page { position: relative; width: 1112px; height: 1200px; }

  .site-header {
    position: absolute; left: 0; top: 0; width: 100%; height: 62px;
    border-bottom: 2px solid var(--accent);
  }
  .brand {
    position: absolute; left: 80px; top: 14px;
    font-size: 24px; font-weight: 400; color: var(--accent);
    letter-spacing: 0.5px;
  }
  .main-nav { position: absolute; top: 19px; left: 0; width: 100%; }
  .main-nav a {
    position: absolute; font-size: 13px; font-weight: 700;
    letter-spacing: 1px; color: var(--ink); text-decoration: none;
  }

  .bio-title {
    position: absolute; left: 80px; top: 100px;
    font-size: 20px; font-weight: 700; letter-spacing: 1.2px;
    text-transform: uppercase; color: var(--ink);
    padding-bottom: 3px; border-bottom: 3px solid var(--accent);
  }
  .bio-text {
    position: absolute; left: 80px; top: 170px; width: 635px;
    font-size: 15px; line-height: 19.8px; color: var(--muted);
    letter-spacing: 0.3px;
  }
  .bio-text p { margin-bottom: 20px; }
  .issue-list { list-style: none; margin-top: -6px; }
  .issue-list li {
    position: relative; padding-left: 16px; height: 28.4px;
  }
  .issue-list li::before {
    content: ""; position: absolute; left: 0; top: 7px;
    width: 8px; height: 8px; border-radius: 50%; background: var(--accent);
  }

  .portrait {
    position: absolute; left: 751px; top: 128px;
    width: 197px; height: 197px; border-radius: 50%;
    background: radial-gradient(circle at 50% 40%, var(--portrait-light) 0%, #9a9a9a 55%, var(--portrait-dark) 100%);
  }
  .contact-card {
    position: absolute; left: 700px; top: 345px; width: 325px;
    text-align: center; font-size: 13.5px; letter-spacing: 0.5px;
  }
  .mail-link {
    display: inline-flex; align-items: center; gap: 8px;
    color: var(--accent); text-decoration: none;
  }
  .email { display: block; margin-top: 5px; color: var(--ink); }

  .site-footer {
    position: absolute; left: 0; top: 1134px; width: 100%; height: 66px;
    background: var(--footer-bg); color: var(--footer-ink);
    font-size: 13px; letter-spacing: 0.8px;
    display: flex; justify-content: center; align-items: center; gap: 22px;
  }
</style>
</head>
<body>
<div class="page">
  <header class="site-header">
    <div class="brand">TBK Law Group</div>
    <nav class="main-nav">
      <a href="#" style="left:615px">HOME</a>
      <a href="#" style="left:693px">ABOUT</a>
      <a href="#" style="left:778px">TEAM</a>
      <a href="#" style="left:853px">EXPERIENCE</a>
      <a href="#" style="left:972px">CONTACT</a>
    </nav>
  </header>

  <h1 class="bio-title">Curtis P. Langford</h1>

  <section class="bio-text">
    <p>Over the years, Curtis has worked with private and public companies in numerous industries, including consumer/retail products and services, various technology sectors (clean-technology, bio-tech, communications and networking, computer hardware and software, electronic), telecommunications, professional and educational services, among others.</p>
    <p>As part of counseling clients regarding all of the legal issues that arise around individual and corporate identities, brands, and reputations, TBK Law Group frequently provides advice with respect to these related issues:</p>
    <ul class="issue-list">
      <li>Advertising and marketing review;</li>
      <li>Copyright use and protection;</li>
      <li>Domain name procurement and recovery;</li>
      <li>Trade secret protection;</li>
      <li>Franchise arrangements;</li>
      <li>Promotions, sweepstakes, and contest rule review/drafting; and</li>
      <li>Sponsorship and endorsement relationships.</li>
    </ul>
  </section>

  <div class="portrait" role="img" aria-label="Black and white portrait photo of Curtis P. Langford"></div>

  <div class="contact-card">
    <a class="mail-link" href="#">
      <svg width="26" height="18" viewBox="0 0 26 18" aria-hidden="true">
        <rect x="1" y="1" width="24" height="16" fill="none" stroke="#f26531" stroke-width="1.5"/>
        <path d="M1 1 L13 10 L25 1 M1 17 L10 8 M25 17 L16 8" fill="none" stroke="#f26531" stroke-width="1.5"/>
      </svg>
      Mail Me
    </a>
    <span class="email">Curtis@tbkcounsel.com</span>
  </div>

  <footer class="site-footer">
    <span>© 2008-2017 TBK LAW GROUP PLLC</span>
    <span>All Rights Reserved</span>
    <span>www.tbkcounsel.com</span>
  </footer>
</div>
</body>
</html>
```